plumweave business card

need to upgrade current business card for an online retailer of handmade arts and crafts, please visit plumweave.com.au

need to be artistic professional look

sample layout, contents, logo, are in the attached files

need for 4 people, details for other 2 people to be provided later

Industry/Entity Type

Business

```html
<!DOCTYPE html>
<html lang="en">
<head>
<meta charset="utf-8">
<title>plumweave business card</title>
<link rel="stylesheet" href="https://fonts.googleapis.com/css2?family=Open+Sans:wght@300;400&family=Tinos:wght@700&display=swap">
<style>
  :root {
    --backdrop: #ececec;
    --card-dark: #1f1f1f;
    --card-light: #fbfbfb;
    --ink-dark: #1c1c1c;
    --ink-grey: #6a6a6a;
    --ink-soft: #8c8c8c;
    --accent: #d0312d;
    --font-text: "Open Sans", Arial, sans-serif;
    --font-display: "Tinos", "Times New Roman", serif;
  }
  * { margin: 0; padding: 0; box-sizing: border-box; }
  html, body { width: 1200px; height: 800px; overflow: hidden; }
  body { background: var(--backdrop); position: relative; font-family: var(--font-text); }

  .card {
    position: absolute;
    width: 500px;
    height: 300px;
    top: 250px;
    box-shadow: 0 6px 18px rgba(0,0,0,0.12);
  }
  .card--back { left: 60px; background: var(--card-dark); color: var(--ink-soft); }
  .card--front { left: 640px; background: var(--card-light); color: var(--ink-grey); }

  /* back side */
  .back-intro { position: absolute; left: 40px; top: 40px; font-size: 14px; font-weight: 300; }
  .offer-list { position: absolute; left: 52px; top: 74px; list-style: none; font-size: 14px; font-weight: 300; line-height: 22px; }
  .offer-list li::before { content: "• "; }
  .back-rule { position: absolute; left: 40px; right: 40px; top: 200px; height: 1px; background: var(--accent); }
  .back-note { position: absolute; left: 40px; top: 212px; font-size: 13px; font-weight: 300; }
  .back-brand { position: absolute; right: 40px; top: 174px; font-family: var(--font-display); font-size: 17px; font-weight: 700; color: var(--accent); }

  /* front side */
  .brand-name { position: absolute; right: 40px; top: 34px; font-family: var(--font-display); font-weight: 700; font-size: 46px; color: var(--ink-dark); letter-spacing: 0.5px; }
  .front-rule { position: absolute; left: 36px; right: 36px; top: 190px; height: 1px; background: var(--accent); }
  .person-name { position: absolute; left: 36px; top: 150px; font-family: var(--font-display); font-weight: 700; font-size: 32px; color: var(--ink-dark); }
  .services-title { position: absolute; left: 320px; top: 168px; font-size: 12px; font-weight: 300; }
  .services-list { position: absolute; left: 320px; top: 198px; list-style: none; font-size: 12px; font-weight: 300; line-height: 18px; }
  .services-list li::before { content: "· "; }
  .contact-list { position: absolute; left: 36px; top: 202px; list-style: none; font-size: 12px; font-weight: 300; line-height: 19px; }
  .contact-list li { display: flex; align-items: center; gap: 8px; }
  .contact-list svg { width: 13px; height: 13px; flex: none; }
</style>
</head>
<body>

<section class="card card--back" aria-label="Card back">
  <p class="back-intro">Visit us for exotic hand-made arts &amp; crafts around the globe</p>
  <ul class="offer-list">
    <li>Cashmere fashion items from Nepal</li>
    <li>Thai Traditional Paintings</li>
    <li>Nepal / Tibetan Thangkas</li>
    <li>Lokta / Rice Paper Crafts</li>
    <li>Allo / Cotton / Woollen Items</li>
  </ul>
  <span class="back-brand">plumweave</span>
  <div class="back-rule"></div>
  <p class="back-note">We encourage eco-friendly, sustainable and traditional arts practice.</p>
</section>

<section class="card card--front" aria-label="Card front">
  <span class="brand-name">plumweave</span>
  <p class="services-title">We do handicrafts:</p>
  <h1 class="person-name">Mohan Basnet</h1>
  <div class="front-rule"></div>
  <ul class="services-list">
    <li>design / promotion</li>
    <li>wholesale / retail</li>
    <li>import / export</li>
  </ul>
  <ul class="contact-list">
    <li>
      <svg viewBox="0 0 16 16" aria-hidden="true"><circle cx="8" cy="8" r="8" fill="var(--accent)"/><path d="M5 4.5l1.6-.5 1 2.3-1 .8a5 5 0 0 0 2.3 2.3l.8-1 2.3 1-.5 1.6c-3.5.3-6.8-3-6.5-6.5z" fill="#fff"/></svg>
      +61 412 508 736
    </li>
    <li>
      <svg viewBox="0 0 16 16" aria-hidden="true"><circle cx="8" cy="8" r="8" fill="var(--accent)"/><circle cx="8" cy="8" r="5" fill="none" stroke="#fff" stroke-width="1"/><ellipse cx="8" cy="8" rx="2.2" ry="5" fill="none" stroke="#fff" stroke-width="1"/><path d="M3 8h10" stroke="#fff" stroke-width="1"/></svg>
      www.plumweave.com.au
    </li>
    <li>
      <svg viewBox="0 0 16 16" aria-hidden="true"><rect x="0" y="2" width="16" height="12" fill="var(--accent)"/><path d="M1 3l7 6 7-6" fill="none" stroke="#fff" stroke-width="1.2"/></svg>
      tara@plumweave.com.au
    </li>
  </ul>
</section>

</body>
</html>
```